Webdesign für Reittherapeutin
Zielgruppe
Ich bin Reittherapeutin und biete auf unserem privaten Hof Reittherapie für Kinder, Jugendliche und Erwachsene an. Die Therapieeinheiten finden im Freien statt, also auf dem Sandplatz oder im Gelände. In der Reittherapie steht nicht das Reiten, sonden der Umgang und die Beziehung zum Pferd im Vordergrund.
Aufgabenstellung
Mir gefallen Designs in Naturtönen, welche auch gut zu meiner Tätigkeit passen. Ich habe bereits ein Logo, einen Namen (Wiesen erleben) und die Domaine (www.wiesen-erleben.ch) ebenso.

```html
<!DOCTYPE html>
<html lang="de">
<head>
<meta charset="utf-8">
<title>Wiesen erleben – Über mich</title>
<link href="https://fonts.googleapis.com/css2?family=Open+Sans:ital,wght@0,400;0,600;1,400;1,600&family=Sofia&display=swap" rel="stylesheet">
<style>
  :root{
    --brown:#76604f;
    --brown-text:#8a6c57;
    --teal:#1b98a3;
    --sand:#ebe3d9;
    --ink:#2b2622;
    --white:#ffffff;
  }
  *{box-sizing:border-box;margin:0;padding:0}
  html,body{width:1200px;height:1064px;overflow:hidden}
  body{position:relative;background:var(--sand);font-family:"Open Sans",Arial,sans-serif;color:var(--ink)}
  .topbar{position:absolute;left:0;top:0;width:1200px;height:29px;background:var(--brown);color:#f3ece5;font-size:12.5px;display:flex;align-items:center;padding-left:192px;gap:16px}
  .topbar span{display:flex;align-items:center;gap:4px}
  .header{position:absolute;left:0;top:29px;width:1200px;height:100px;background:var(--white)}
  .brand{position:absolute;left:186px;top:12px;display:flex;align-items:center;gap:12px}
  .brand-dot{width:64px;height:64px;border-radius:50%;background:var(--teal)}
  .brand-name{font-size:26px;font-weight:400;color:var(--brown)}
  .nav{position:absolute;top:36px;left:683px;display:flex;gap:21px;font-size:12.5px}
  .nav a{color:var(--ink);text-decoration:none}
  .nav a.active{color:var(--teal)}
  .hero{position:absolute;left:0;top:120px;width:1200px;height:385px}
  .horse-deco{position:absolute;left:940px;top:590px;width:260px;height:350px;background:radial-gradient(ellipse at 60% 45%,rgba(255,255,255,.85),rgba(255,255,255,0) 70%)}
  .about{position:absolute;left:200px;top:522px;width:790px}
  .about h1{font-family:"Sofia",cursive;font-weight:400;font-size:28px;color:var(--ink);line-height:1.3}
  .about .rule{width:62px;height:2px;background:var(--teal);margin-top:4px;margin-bottom:20px}
  .about p{font-size:12.6px;line-height:18.7px;letter-spacing:.3px;margin-bottom:10.6px}
  .about em{color:var(--brown-text);font-weight:600}
  .cta{position:absolute;left:197px;top:847px;width:222px;height:36px;border-radius:18px;background:var(--teal);border:1.5px solid var(--white);color:var(--white);font-size:11.3px;display:flex;align-items:center;justify-content:center;letter-spacing:.2px}
  .social{position:absolute;left:0;top:587px;width:36px}
  .social span{display:block;width:36px;height:36px}
  .s1{background:#3b5998}.s2{background:#55acee}.s3{background:#dc4e41}.s4{background:#0077b5}
  .wave{position:absolute;left:0;top:920px}
  .totop{position:absolute;left:1116px;top:929px;width:44px;height:44px;border-radius:50%;background:var(--teal);display:flex;align-items:center;justify-content:center}
  .legal{position:absolute;left:203px;top:1001px;font-size:11.5px;color:var(--ink)}
  .footer{position:absolute;left:0;top:1024px;width:1200px;height:40px;background:var(--brown);color:#f3ece5;font-size:11.5px;padding-left:203px;display:flex;align-items:center}
</style>
</head>
<body>
  <div class="topbar">
    <span><svg width="12" height="10" viewBox="0 0 12 10"><rect x=".7" y=".7" width="10.6" height="8.6" fill="none" stroke="#f3ece5" stroke-width="1.2"/><path d="M1 1l5 4 5-4" fill="none" stroke="#f3ece5" stroke-width="1.2"/></svg>info@wiesen-erleben.ch</span>
    <span><svg width="10" height="10" viewBox="0 0 10 10"><path d="M2 0l2 2.5-1 1.5c.7 1.4 1.6 2.3 3 3l1.5-1L10 8l-1.5 2C4 9.5.5 6 0 1.5z" fill="#f3ece5"/></svg>0041 79 000 12 34</span>
  </div>

  <header class="header">
    <div class="brand"><span class="brand-dot"></span><span class="brand-name">Wiesen erleben</span></div>
    <nav class="nav">
      <a href="#">Reittherapie</a><a href="#">Angebot</a><a href="#" class="active">Über mich</a><a href="#">Pferde</a><a href="#" class="active">Kontakt</a>
    </nav>
  </header>

  <svg class="hero" viewBox="0 0 1200 385" width="1200" height="385">
    <defs>
      <linearGradient id="sky" x1="0" y1="0" x2="0" y2="1">
        <stop offset="0" stop-color="#9ec3ea"/>
        <stop offset=".45" stop-color="#b9c9c9"/>
        <stop offset=".6" stop-color="#8a8a63"/>
        <stop offset="1" stop-color="#4d4638"/>
      </linearGradient>
    </defs>
    <path d="M0 16 C200 0 350 0 600 30 C850 60 1000 55 1200 22 L1200 60 C1000 90 800 80 600 55 C350 25 200 20 0 40Z" fill="var(--brown)"/>
    <path d="M0 32 C200 12 350 15 600 40 C850 65 1000 62 1200 30 L1200 60 C1000 90 800 85 600 60 C350 35 200 30 0 52Z" fill="var(--teal)"/>
    <path role="img" aria-label="Foto: Therapeutin mit schwarzem Pony und liegender Reiterin auf der Weide" d="M0 50 C200 30 350 35 600 62 C850 90 1000 82 1200 30 L1200 340 C1000 360 800 355 600 340 C350 320 200 325 0 360Z" fill="url(#sky)"/>
    <path d="M0 360 C200 325 350 320 600 340 C800 355 1000 360 1200 335 L1200 385 L0 385Z" fill="var(--brown)"/>
    <path d="M0 362 C200 328 350 322 600 338 C800 350 1000 352 1200 333 L1200 355 C1000 372 800 370 600 360 C350 345 200 345 0 372Z" fill="var(--teal)"/>
    <path d="M0 370 C200 342 350 340 600 352 C800 362 1000 372 1200 362 L1200 385 L0 385Z" fill="var(--sand)"/>
  </svg>

  <div class="horse-deco" role="img" aria-label="Helle Silhouette eines Pferdes mit Schmetterlingen"></div>

  <nav class="social" aria-label="Teilen"><span class="s1"></span><span class="s2"></span><span class="s3"></span><span class="s4"></span></nav>

  <section class="about">
    <h1>Über mich</h1>
    <div class="rule"></div>
    <p>Im 2019 durfte ich die <em>Ausbildung zur Reittherapeutin</em> erfolgreich abschliessen und meinen Traum, zusammen mit meinen Pferden anderen Menschen etwas Gutes zu tun, wahr werden lassen.</p>
    <p>Mein grosser Wunsch ist es, Kindern, Jugendlichen und auch Erwachsenen, die bereit sind, sich in <em>entspannter Atmosphäre</em> dem Pferd zu nähern, das Wesen Pferd und seine <em>wunderbaren Eigenschaften</em> näher zu bringen.</p>
    <p>Dabei sollen die Freude, der Spass und die <em>Beziehung zum Pferd</em> im Vordergrund stehen.</p>
    <p>Die Pferde und ihre <em>Faszination</em> begleiten mich seit meiner Kindheit und begeistern und erfreuen mich bis heute.</p>
    <p>Ich habe das grosse Glück, mit meiner Familie und den Pferden <em>mitten im Naherholungsgebiet des Auenfeldes</em> zu Hause zu sein.</p>
    <p>Unmittelbar angrenzend an unser Grundstück liegt das grösste Auengebiet des Schweizer Mittellandes.</p>
    <p>Dieses bietet eine <em>wunderbare Natur</em>, <em>Erholung und Ruhe</em>.</p>
  </section>

  <a class="cta">Nehmen SIe jetzt mit mir Kontakt auf</a>

  <svg class="wave" width="1200" height="60" viewBox="0 0 1200 60"><path d="M260 12 C500 8 800 30 1000 38 C1100 42 1160 36 1200 30 L1200 44 C1100 52 1000 52 880 48 C650 40 450 14 260 12Z" fill="var(--white)"/></svg>

  <div class="totop"><svg width="22" height="14" viewBox="0 0 22 14"><path d="M2 12l9-9 9 9" fill="none" stroke="#fff" stroke-width="3.5"/></svg></div>

  <div class="legal">Datenschutz | Impressum | AGB’s</div>
  <footer class="footer">Copyright© Nadja Brunner</footer>
</body>
</html>
```